LABEL DESIGNS FOR SKINCARE LINE

Hello we are needing 12 label various label designs but would like to see you design ONE. We will pick winner from this and send the rest.
LABEL SIZE -2x7
JAR SIZE IS - 8oz
LOGOS FILES BELOW
https://files.pavorna-share.net/drive/folders/7xk3q-wumTrazPLoqVnnRTZBKHAE2DpLW
INFORMATION FOR LABEL
Calm Dune Hush Whipped Body Sugar Scrub 8oz
Ideal for all Skin Types
Ingredients:
Pure Cane Sugar, Extra Virgin Coconut Oil, Mango Butter, Kukum Butter, Emulsifying Wax, Jojoba Seed Oil, Sweet Almond Oil, Strawberry Essential Oil, and Pomegranate Essential Oil.
Directions to use Body Sugar Scrub:
Apply to wet skin gently in a circular motion on desired body area, hands, feet, legs, arms, etc. Once you have a good scrub, rinse, pat dry, and enjoy soft, hydrated skin. Best to use in the shower. Use between 2-3 times a week if needed.
*Cautions:
(1) Allergy: Approach this product with extreme caution, if you have allergies
(2) Avoid direct contact with eyes
Storage/Shelf Life of Product:
For best results, stir/mix scrub with the wooden or plastic spoon before each use. The shelf life of all sugar scrubs is 6-8 weeks. Keep the product in a cool, dry place, away from hot or heated temperatures.
All Natural, Cruelty-Free, Vegan Free
No Mineral Oil
No Petroleum
No Parabens

```html
<!DOCTYPE html>
<html lang="en">
<head>
<meta charset="utf-8">
<title>Calm Dune Hush Whipped Body Sugar Scrub – Jar Label</title>
<link href="https://fonts.googleapis.com/css2?family=Source+Sans+3:ital,wght@0,300;0,400;0,600;0,700;1,400&family=PT+Sans+Narrow&display=swap" rel="stylesheet">
<style>
  :root {
    --page: #ffffff;
    --label: #ef9f82;
    --label-center: #f0a287;
    --ink-light: #ffffff;
    --accent: #e5622d;
  }
  * { box-sizing: border-box; margin: 0; padding: 0; }
  html, body {
    width: 1200px; height: 1200px; overflow: hidden;
    background: var(--page);
  }
  .canvas {
    position: relative; width: 1200px; height: 1200px;
    font-family: "Source Sans 3", "Helvetica Neue", Arial, sans-serif;
    color: var(--ink-light);
  }
  .label-strip {
    position: absolute; left: 30px; top: 442px;
    width: 1140px; height: 316px;
    display: flex;
  }
  .panel { position: relative; height: 100%; background: var(--label); }
  .panel--back-left { width: 319px; }
  .panel--front { width: 504px; background: var(--label-center); }
  .panel--back-right { width: 317px; }

  /* left panel */
  .cautions {
    position: absolute; left: 28px; right: 20px; top: 28px;
    font-size: 11.5px; font-weight: 700; line-height: 1.15;
    text-transform: uppercase; text-align: justify;
  }
  .cautions__title { color: var(--accent); }
  .storage {
    position: absolute; left: 28px; right: 20px; top: 123px;
    font-size: 11.4px; font-weight: 300; line-height: 1.35;
    text-align: justify;
  }
  .claims {
    position: absolute; left: 28px; top: 228px;
    font-size: 11.6px; font-weight: 700; line-height: 1.32;
    text-transform: uppercase; list-style: none;
  }

  /* front panel */
  .brand {
    position: absolute; left: 131px; top: 68px;
    font-size: 33px; font-weight: 700; color: var(--accent);
    letter-spacing: 0.5px; line-height: 1;
  }
  .brand-rule {
    position: absolute; left: 131px; top: 115px;
    width: 239px; height: 3px; background: var(--accent);
  }
  .product-name {
    position: absolute; left: 131px; top: 136px;
    font-size: 25px; line-height: 1.13; font-weight: 300;
    text-transform: uppercase;
  }
  .product-name strong { font-weight: 700; }
  .product-name .accent { color: var(--accent); font-weight: 700; }
  .skin-types {
    position: absolute; left: 131px; top: 240px;
    font-family: "PT Sans Narrow", "Arial Narrow", sans-serif;
    font-size: 22px; color: var(--accent);
  }
  .net-weight {
    position: absolute; left: 135px; top: 292px;
    font-size: 7.5px; font-weight: 600;
  }

  /* right panel */
  .ingredients {
    position: absolute; left: 16px; right: 27px; top: 26px;
    font-size: 15.5px; line-height: 1.13; text-align: justify;
  }
  .ingredients__title { font-weight: 300; }
  .ingredients__list { font-style: italic; }
  .directions {
    position: absolute; left: 16px; right: 27px; top: 168px;
    font-size: 13.4px; line-height: 1.3;
  }
  .directions__title { font-weight: 300; display: block; margin-bottom: 1px; }
  .directions__text { font-style: italic; }
</style>
</head>
<body>
<main class="canvas">
  <section class="label-strip" aria-label="Flat jar label">
    <div class="panel panel--back-left">
      <div class="cautions">
        <p class="cautions__title">*Cautions:</p>
        <p>(1) Allergy: Approach this product with extreme caution, if you have allergies</p>
        <p>(2) Avoid direct contact with eyes</p>
      </div>
      <p class="storage">STORAGE/SHELF LIFE OF PRODUCT: For best results, stir/mix scrub with the wooden or plastic spoon before each use. The shelf life of all sugar scrubs is 6-8 weeks. Keep the product in a cool, dry place, away from hot or heated temperatures.</p>
      <ul class="claims">
        <li>All Natural, Cruelty-Free, Vegan Free</li>
        <li>No Mineral Oil</li>
        <li>No Petroleum</li>
        <li>No Parabens</li>
      </ul>
    </div>

    <div class="panel panel--front">
      <p class="brand">Tansy Row</p>
      <div class="brand-rule"></div>
      <h1 class="product-name">
        Calm <strong>Dune</strong><br>
        Hush <strong>Whipped</strong><br>
        <strong>Body Sugar</strong> <span class="accent">Scrub</span>
      </h1>
      <p class="skin-types">Ideal for all Skin Types</p>
      <p class="net-weight">240 mL ⊖ Net Wt. 8 oz.</p>
    </div>

    <div class="panel panel--back-right">
      <p class="ingredients">
        <span class="ingredients__title">INGREDIENTS:</span>
        <span class="ingredients__list">Pure Cane Sugar, Extra Virgin Coconut Oil, Mango Butter, Kukum Butter, Emulsifying Wax, Jojoba Seed Oil, Sweet Almond Oil, Strawberry Essential Oil, and Pomegranate Essential Oil.</span>
      </p>
      <p class="directions">
        <span class="directions__title">DIRECTIONS TO USE BODY SUGAR SCRUB:</span>
        <span class="directions__text">Apply to wet skin gently in a circular motion on desired body area, hands, feet, legs, arms, etc. Once you have a good scrub, rinse, pat dry, and enjoy soft, hydrated skin. Best to use in the shower. Use between 2-3 times a week if needed.</span>
      </p>
    </div>
  </section>
</main>
</body>
</html>
```